Business Card Design for ReaL ESTATE AGENT

New Business Cards for a real estate agent in Jacksonville, FL. My specialty is urban core, historic districts but sell through out the city. Company Name is Quill and Harbor Realty a division of the Vantrell Companies. The card needs to convey an essence of professionalism, knowledge and success.

Target Market(s)

Home buyers and Sellers

Industry/Entity Type

Real Estate

Contact Information for Business Card

Double sided

Font styles to use
Sans Serif

Requirements
Must have
• My logs and photo (provided). My contact information as follows:
• Derek Holloway
• Cell 904-618-3092
• Office 904-731-6248
• Email derekholloway@mailvantor.com
Nice to have
• Tag Line - Exceptional Effort. Proven Results.

```html
<!DOCTYPE html>
<html lang="en">
<head>
<meta charset="utf-8">
<title>Derek Holloway – Business Card</title>
<link href="https://fonts.googleapis.com/css2?family=Open+Sans:wght@400;600;700&display=swap" rel="stylesheet">
<style>
  :root {
    --green: #1f6b4b;
    --green-dark: #0f4a32;
    --green-light: #2f8a63;
    --red: #e0473a;
    --text-grey: #4a4a4a;
    --paper: #ffffff;
    --stage: #e9ebea;
  }
  * { margin: 0; padding: 0; box-sizing: border-box; }
  html, body {
    width: 1200px; height: 913px; overflow: hidden;
    background: var(--stage);
    font-family: "Open Sans", sans-serif;
  }
  .canvas { position: relative; width: 1200px; height: 913px; }
  .card {
    position: absolute; top: 308px;
    width: 520px; height: 298px;
    border-radius: 14px; overflow: hidden;
    box-shadow: 0 6px 18px rgba(0,0,0,.18);
  }
  .card--front { left: 50px; background: var(--paper); }
  .card--back {
    left: 630px;
    background: linear-gradient(160deg, var(--green-light) 0%, var(--green) 45%, var(--green-dark) 100%);
    display: flex; align-items: center; justify-content: center;
  }
  .corner-tab { position: absolute; top: 0; right: 0; width: 40px; height: 14px; background: var(--green); }
  .corner-tab::before {
    content: ""; position: absolute; left: -5px; top: 0; width: 3px; height: 14px; background: var(--red);
  }
  .agent { position: absolute; top: 20px; right: 52px; text-align: right; }
  .agent__name { color: var(--green); font-weight: 700; font-size: 22px; line-height: 1.1; }
  .agent__title { color: var(--red); font-size: 11px; margin-top: 2px; }
  .rule { position: absolute; top: 72px; left: 150px; width: 170px; height: 1px; background: var(--green); }
  .portrait {
    position: absolute; top: 70px; right: 0; width: 230px; height: 170px;
    background: linear-gradient(180deg, #d9d4cf 0%, #b9b3ad 45%, #2f3033 100%);
  }
  .bands { position: absolute; left: 0; bottom: 0; width: 520px; height: 120px; }
  .brand {
    position: absolute; top: 96px; left: 26px;
    display: flex; align-items: center; gap: 8px;
  }
  .brand__mark { width: 14px; height: 14px; background: var(--green); }
  .brand__name { color: var(--green); font-weight: 700; font-size: 17px; }
  .contacts { position: absolute; top: 150px; left: 30px; list-style: none; }
  .contacts li {
    display: flex; align-items: center; gap: 8px;
    color: var(--text-grey); font-size: 12.5px; line-height: 18px;
  }
  .contacts svg { width: 11px; height: 11px; flex: none; }
  .back-brand { display: flex; align-items: center; gap: 12px; }
  .back-brand__mark { width: 22px; height: 22px; background: #ffffff; }
  .back-brand__name { color: #ffffff; font-weight: 700; font-size: 28px; }
</style>
</head>
<body>
<div class="canvas">
  <section class="card card--front">
    <div class="corner-tab"></div>
    <div class="agent">
      <div class="agent__name">Derek Holloway</div>
      <div class="agent__title">Realtor</div>
    </div>
    <div class="rule"></div>
    <div class="portrait" role="img" aria-label="Portrait photograph of the agent in a dark suit and red tie"></div>
    <svg class="bands" viewBox="0 0 520 120" preserveAspectRatio="none" aria-hidden="true">
      <path d="M0 112 C160 100 300 70 400 40 C450 26 490 22 520 20 L520 120 L0 120 Z" fill="#e0473a"/>
      <path d="M0 108 C170 104 310 80 410 54 C460 42 495 38 520 36 L520 120 L0 120 Z" fill="#1f6b4b"/>
      <path d="M0 114 C180 112 320 92 420 70 C465 60 500 56 520 56 L520 120 L0 120 Z" fill="#0f4a32" opacity=".55"/>
    </svg>
    <div class="brand">
      <span class="brand__mark"></span>
      <span class="brand__name">Quill and Harbor Realty</span>
    </div>
    <ul class="contacts">
      <li>
        <svg viewBox="0 0 12 12"><path d="M2 1l2 0 1 3-1.5 1a6 6 0 0 0 3 3L8 7l3 1 0 2c0 .6-.4 1-1 1A9 9 0 0 1 1 2c0-.6.4-1 1-1z" fill="#e0473a"/></svg>
        904-731-6248
      </li>
      <li>
        <svg viewBox="0 0 12 12"><rect x="3" y="1" width="6" height="10" rx="1" fill="none" stroke="#e0473a" stroke-width="1.3"/><circle cx="6" cy="9" r=".7" fill="#e0473a"/></svg>
        904-618-3092
      </li>
      <li>
        <svg viewBox="0 0 12 12"><rect x="1" y="2.5" width="10" height="7" fill="none" stroke="#e0473a" stroke-width="1.2"/><path d="M1 2.5l5 4 5-4" fill="none" stroke="#e0473a" stroke-width="1.2"/></svg>
        derekholloway@mailvantor.com
      </li>
      <li>
        <svg viewBox="0 0 12 12"><circle cx="6" cy="6" r="5" fill="none" stroke="#e0473a" stroke-width="1.1"/><path d="M1 6h10M6 1c2 2.5 2 7.5 0 10M6 1c-2 2.5-2 7.5 0 10" fill="none" stroke="#e0473a" stroke-width=".9"/></svg>
        www.derekhollowayhomes.com
      </li>
    </ul>
  </section>

  <section class="card card--back">
    <div class="back-brand">
      <span class="back-brand__mark"></span>
      <span class="back-brand__name">Quill and Harbor Realty</span>
    </div>
  </section>
</div>
</body>
</html>
```